White Rum brand needs bottle label

Looking for a label that will stand out on a shelf and feel like an instant classic. Corvane is a premium Caribbean blended white rum that was crafted as an escape from day-to-day stress and is all about making each day feel as though it's a vacation day. It was named after two local beaches and surf breaks both of which are party towns. I'd like the label to feel modern, sleek, and casual, while still feeling very slightly upscale and have a few subtle hints of it's tropical origin. Corvane should look suitable to drink in variety of situations such as a casual drink at the beach or a pool, a cocktail after a long day of work, or a night out at a bar or club. Please incorporate the logo somewhere in the label, whether that's just the mermaid or the entire design I'll leave that up to the designer. Whatever it is, it should have a look that is scalable and feels appropriate to consume in many settings while remembering it's Carribean and beach roots.

Target Market(s)

The target market is fairly broad. Target consumers are between 21-55, leaning slightly more towards the masculine crowd, full-time workers that enjoy drinking regularly.

Font styles to use
Serif
Sans Serif

Requirements
Must have
• Must have at least the mermaid part of the logo incorporated within the label.
Nice to have
• I'd like a bottle with a synthetic cork, that has a strap sealer over the top and a bottle shaped similar to Valdoro Tequila. Colors are designer's choice. Subtle floral or tropical notes (not too much) mixed into a fairly sleek and modern design.

```html
<!DOCTYPE html>
<html lang="en">
<head>
<meta charset="utf-8">
<title>Corvane Premium White Rum – Label</title>
<link rel="stylesheet" href="https://fonts.googleapis.com/css2?family=Montserrat:wght@300;400;800&family=Oswald:wght@300&display=swap">
<style>
  :root {
    --page: #f3f2f0;
    --navy: #2d3a58;
    --navy-deep: #253049;
    --navy-soft: #5d6d8e;
    --slate: #8e9ab3;
    --gold: #d2a95a;
    --gold-deep: #b38a3e;
    --white: #ffffff;
    --aqua: #8fd3e6;
  }
  * { box-sizing: border-box; margin: 0; padding: 0; }
  html, body {
    width: 960px; height: 1200px; overflow: hidden;
    background: var(--page);
  }
  .canvas {
    position: relative; width: 960px; height: 1200px;
  }
  .label {
    position: absolute; left: 162px; top: 80px;
    width: 636px; height: 1040px;
    background: var(--navy);
    overflow: hidden;
    color: var(--white);
    font-family: "Montserrat", sans-serif;
  }
  .label__art {
    position: absolute; inset: 0;
  }
  .label__content {
    position: absolute; inset: 0;
    text-align: center;
  }
  .emblem {
    position: absolute; left: 50%; top: 150px;
    width: 200px; height: 200px; margin-left: -100px;
    border-radius: 50%;
    background: radial-gradient(circle at 50% 45%, #e9c86f 0%, var(--gold) 45%, var(--gold-deep) 100%);
    opacity: 0.9;
  }
  .brand-name {
    position: absolute; left: 0; right: 0; top: 410px;
    font-weight: 800; font-size: 96px; letter-spacing: 1px;
    line-height: 1;
  }
  .rule {
    position: absolute; left: 50%; width: 76px; margin-left: -38px;
    height: 2px; background: var(--white);
  }
  .rule--top { top: 640px; }
  .rule--bottom { top: 866px; }
  .tier {
    position: absolute; left: 0; right: 0; top: 675px;
    font-weight: 400; font-size: 35px; color: var(--aqua);
    line-height: 1;
  }
  .spirit {
    position: absolute; left: 0; right: 0; top: 730px;
    font-weight: 800; font-size: 58px; letter-spacing: 1px;
    line-height: 1;
  }
  .origin {
    position: absolute; left: 0; right: 0; top: 798px;
    font-weight: 400; font-size: 33px;
    line-height: 1;
  }
  .specs {
    position: absolute; left: 0; right: 0; top: 950px;
    font-family: "Oswald", sans-serif; font-weight: 300;
    font-size: 30px; letter-spacing: 4px;
    line-height: 1;
  }
  .specs .sep { font-weight: 300; padding: 0 4px; }
</style>
</head>
<body>
<main class="canvas">
  <section class="label">
    <svg class="label__art" viewBox="0 0 636 1040" width="636" height="1040" role="img" aria-label="Abstract brush strokes and soft tropical shapes in navy, slate and gold">
      <defs>
        <linearGradient id="wash" x1="0" y1="0" x2="1" y2="1">
          <stop offset="0" stop-color="#33405f"/>
          <stop offset="0.5" stop-color="#4a5a7c"/>
          <stop offset="1" stop-color="#263149"/>
        </linearGradient>
      </defs>
      <rect width="636" height="1040" fill="url(#wash)"/>
      <path d="M380 0 H636 V420 C560 380 520 300 470 220 C430 160 390 90 380 0 Z" fill="#62739a" opacity="0.55"/>
      <path d="M490 0 H636 V170 C580 200 530 170 500 120 C480 80 480 40 490 0 Z" fill="#d2a95a"/>
      <path d="M0 760 C60 790 110 860 170 890 C240 920 300 990 300 1040 H0 Z" fill="#3e5a8f" opacity="0.6"/>
      <path d="M0 120 C60 150 120 180 180 130 V260 C120 300 60 320 0 300 Z" fill="#c9d0de" opacity="0.35"/>
    </svg>
    <div class="label__content">
      <div class="emblem" role="img" aria-label="Gold mermaid emblem"></div>
      <h1 class="brand-name">Corvane</h1>
      <span class="rule rule--top"></span>
      <p class="tier">PREMIUM</p>
      <h2 class="spirit">WHITE RUM</h2>
      <p class="origin">CARIBBEAN BLENDED</p>
      <span class="rule rule--bottom"></span>
      <p class="specs">40% ALC/VOL<span class="sep">|</span>750 ml<span class="sep">|</span>80 PROOF</p>
    </div>
  </section>
</main>
</body>
</html>
```